"Fern Hollow" Soap Box Design with floral corner scroll broder with birds, hand drawn style

I updated the design to REMOVE the words PEACE, also the layout is a horizontal rectangle (landscape design).
I need a front design for a soap box that is 3.5 inches by 2.5 inches in a horizontal / Landscape orientation.
Can you design the box with product information and artwork similar to what I attached? I am not artistic, so what I sent was just done in Microsoft Word.
I prefer a simple hand drawn style for the floral corner borders with small colorful cartoon birds in the borders using vibrant colors rather than soft pastels.
The file needs to be transparent (no background) so it can be placed on different color backgrounds.
Please respond with any questions.
Thank you for your time.

Target Market(s)

women 21-65

Industry/Entity Type

Soap

Font styles to use
Serif
Decorative

Requirements
Must have
• Corner floral borders with cute hand drawn style flowers and birds in bright vibrant happy colors. The logo is wings with "fern hollow". If you can make nicer wings, that would be nice.
Should not have
• The color gray.

```html
<!DOCTYPE html>
<html lang="en">
<head>
<meta charset="utf-8">
<title>Fern Hollow Soap – Box Front Options</title>
<link rel="stylesheet" href="https://fonts.googleapis.com/css2?family=Nunito+Sans:wght@400&display=swap">
<style>
  :root {
    --backdrop: #9d9e9e;
    --label: #ffffff;
    --ink: #231f20;
  }
  * { margin: 0; padding: 0; box-sizing: border-box; }
  html, body {
    width: 977px;
    height: 1200px;
    overflow: hidden;
    background: var(--backdrop);
    font-family: "Nunito Sans", sans-serif;
    font-weight: 400;
    color: var(--ink);
  }
  .sheet { position: relative; width: 977px; height: 1200px; }
  .label {
    position: absolute;
    left: 130px;
    width: 716px;
    height: 512px;
    background: var(--label);
    overflow: hidden;
  }
  .label--first { top: 64px; }
  .label--second { top: 624px; }

  .corner-border {
    position: absolute;
    top: 0;
    width: 240px;
    height: 294px;
  }
  .corner-border--left { left: 0; }
  .corner-border--right { right: 0; transform: scaleX(-1); }

  .brand-mark {
    position: absolute;
    left: 50%;
    width: 40px;
    height: 40px;
    border: 2px solid var(--ink);
    border-radius: 50%;
    transform: translate(-50%, -50%);
  }

  .line {
    position: absolute;
    left: 50%;
    transform: translate(-50%, -50%);
    white-space: nowrap;
    text-align: center;
    line-height: 1;
    font-weight: 400;
  }
  .brand-name { font-size: 36px; letter-spacing: 0.3px; }
  .label--second .brand-name { font-size: 38px; }
  .ingredients { font-size: 19px; }
  .divider {
    position: absolute;
    left: 237px;
    width: 242px;
    height: 2px;
    background: var(--ink);
  }
  .product-type { font-size: 22px; }
  .origin { font-size: 19px; }
  .weight { font-size: 23px; }
</style>
</head>
<body>
<main class="sheet">

  <svg width="0" height="0" style="position:absolute" aria-hidden="true">
    <defs>
      <linearGradient id="bloom-tones" x1="0" y1="0" x2="0.6" y2="1">
        <stop offset="0" stop-color="#f2c6b9"/>
        <stop offset="0.35" stop-color="#b9d6e8"/>
        <stop offset="0.65" stop-color="#e9a0b6"/>
        <stop offset="1" stop-color="#a9a6d4"/>
      </linearGradient>
    </defs>
  </svg>

  <section class="label label--first">
    <svg class="corner-border corner-border--left" viewBox="0 0 240 294" role="img" aria-label="Hand drawn floral corner border with colourful cartoon birds, flowers and hearts">
      <path d="M2 2 H239 V31 H147 V291 H2 Z" fill="url(#bloom-tones)"/>
    </svg>
    <svg class="corner-border corner-border--right" viewBox="0 0 240 294" role="img" aria-label="Hand drawn floral corner border with colourful cartoon birds, flowers and hearts">
      <path d="M2 2 H239 V31 H147 V291 H2 Z" fill="url(#bloom-tones)"/>
    </svg>

    <div class="brand-mark" style="top:124px" aria-hidden="true"></div>
    <h1 class="line brand-name" style="top:212px">FERN HOLLOW SOAP</h1>
    <p class="line ingredients" style="top:342px">HONEY - ALOE-SHEA BUTTER - GOAT MILK</p>
    <div class="divider" style="top:362px"></div>
    <p class="line product-type" style="top:390px">HANDMADE NATURAL SOAP</p>
    <p class="line origin" style="top:422px">NEW YORK</p>
    <p class="line weight" style="top:464px">4 oz</p>
  </section>

  <section class="label label--second">
    <svg class="corner-border corner-border--left" viewBox="0 0 240 294" role="img" aria-label="Hand drawn floral corner border with colourful cartoon birds, flowers and hearts">
      <path d="M2 2 H239 V31 H147 V291 H2 Z" fill="url(#bloom-tones)"/>
    </svg>
    <svg class="corner-border corner-border--right" viewBox="0 0 240 294" role="img" aria-label="Hand drawn floral corner border with colourful cartoon birds, flowers and hearts">
      <path d="M2 2 H239 V31 H147 V291 H2 Z" fill="url(#bloom-tones)"/>
    </svg>

    <div class="brand-mark" style="top:136px" aria-hidden="true"></div>
    <h1 class="line brand-name" style="top:251px">FERN HOLLOW SOAP</h1>
    <p class="line ingredients" style="top:352px">HONEY - ALOE-SHEA BUTTER - GOAT MILK</p>
    <div class="divider" style="top:373px"></div>
    <p class="line product-type" style="top:401px">HANDMADE NATURAL SOAP</p>
    <p class="line origin" style="top:433px">NEW YORK</p>
    <p class="line weight" style="top:475px">4 oz</p>
  </section>

</main>
</body>
</html>
```